Mobile Recording Studio needs business cards

Open to seeing a creative design, but I want to emphasis my logo and minimize the name/title and company information. Possible a fully black background on card.

My company is a mobile sound recording studio. ok to include a my trailer (actual or cartoon) on the card. My initial thought is more straight forward, but a good design will win me over.

SPECS:
CMYK color mode
High (300ppi) raster effect.
cover bleed area
please deliver: Illustrator file with layers and a pdf at completion.

Name and info for the business card:

Dallin Perry
ADR Mixer

email: Dallin@MixVault.com

address:
248 - 5170 East Hollister
Vancouver, BC V5R 2J4

phone:
604.518.2093 office

website:
www.MixVault.com

FB: @MixVault

Instagram: @TheMixVault

Industry/Entity Type

Television Production

Contact Information for Business Card

Dallin Perry
ADR Mixer

email: Dallin@MixVault.com

address:
248 - 5170 East Hollister
Vancouver, BC V5R 2J4

phone:
604.518.2093 office

website:
www.MixVault.com

FB: @MixVault

Instagram: @TheMixVault

Colors

Designer to choose colors to be used in the design.

Requirements
Must have
• emphasis my logo and minimize the name/title and company information.
• SPECS:
• CMYK color mode
• High (300ppi) raster effect.
• cover bleed area
• please deliver: Illustrator file with layers and a pdf at completion.
Nice to have
• maybe include the following:
• all black background or black theme
• my work trailer (actual or cartoon) refer to Instagram: @TheMixVault

```html
<!DOCTYPE html>
<html lang="en">
<head>
<meta charset="utf-8">
<title>MixVault Business Cards</title>
<link href="https://fonts.googleapis.com/css2?family=Montserrat:wght@300;400;700&family=Cinzel:wght@700&display=swap" rel="stylesheet">
<style>
  :root {
    --backdrop: #26272b;
    --card-black: #0a0a0b;
    --silver: #d4d6d9;
    --silver-dark: #8d9095;
    --text-white: #f2f2f2;
    --text-muted: #c9c9c9;
    --photo-dark: #1c1c1a;
    --photo-mid: #4a4a44;
  }
  * { box-sizing: border-box; margin: 0; padding: 0; }
  html, body { width: 1200px; height: 900px; overflow: hidden; }
  body {
    background: var(--backdrop);
    font-family: "Montserrat", sans-serif;
    position: relative;
  }
  .card {
    position: absolute;
    width: 600px;
    height: 343px;
    left: 300px;
    border-radius: 22px;
    background: var(--card-black);
    overflow: hidden;
    box-shadow: 0 14px 30px rgba(0,0,0,0.45);
  }
  .card--front { top: 70px; }
  .card--back { top: 487px; }

  .front-art { position: absolute; inset: 0; }

  .brand-mark {
    font-family: "Cinzel", serif;
    font-weight: 700;
    color: var(--silver);
    letter-spacing: 1px;
    line-height: 1;
  }
  .front-brand {
    position: absolute;
    left: 38px;
    top: 44px;
    font-size: 44px;
  }
  .back-brand {
    position: absolute;
    left: 0; right: 0;
    top: 50%;
    transform: translateY(-50%);
    text-align: center;
    font-size: 60px;
  }

  .contact-block {
    position: absolute;
    right: 34px;
    top: 34px;
    text-align: right;
    color: var(--text-white);
    text-transform: uppercase;
  }
  .person { margin-bottom: 8px; }
  .person-name { font-size: 17px; font-weight: 300; letter-spacing: 0.5px; }
  .person-name strong { font-weight: 700; }
  .person-role { font-size: 9px; font-weight: 400; color: var(--text-muted); letter-spacing: 0.6px; margin-top: 2px; line-height: 1.35; }

  .detail-row {
    display: flex;
    justify-content: flex-end;
    align-items: center;
    gap: 10px;
    font-size: 11.5px;
    font-weight: 400;
    letter-spacing: 0.3px;
    line-height: 1.35;
  }
  .detail-row + .detail-row { margin-top: 8px; }
  .address { margin-top: 14px; }
  .icon { width: 16px; height: 16px; flex: none; }

  .social-row {
    position: absolute;
    right: 34px;
    bottom: 26px;
    display: flex;
    gap: 26px;
    color: var(--text-white);
    font-size: 10px;
    letter-spacing: 0.3px;
  }
  .social-handle { display: flex; align-items: center; gap: 6px; }
  .social-dot { width: 11px; height: 11px; border-radius: 50%; background: var(--text-muted); }
</style>
</head>
<body>

<section class="card card--front" aria-label="Business card front">
  <svg class="front-art" width="600" height="343" viewBox="0 0 600 343">
    <defs>
      <linearGradient id="trailerTone" x1="0" y1="0" x2="1" y2="1">
        <stop offset="0" stop-color="var(--photo-mid)"/>
        <stop offset="1" stop-color="var(--photo-dark)"/>
      </linearGradient>
    </defs>
    <polygon points="0,0 300,0 140,343 0,343" fill="url(#trailerTone)" role="img" aria-label="Photo of the mobile recording trailer"/>
    <line x1="300" y1="0" x2="140" y2="343" stroke="var(--silver)" stroke-width="3"/>
  </svg>

  <div class="brand-mark front-brand">MixVault</div>

  <div class="contact-block">
    <div class="person">
      <div class="person-name"><strong>Dallin</strong> Perry</div>
      <div class="person-role">ADR Mixer</div>
    </div>
    <div class="person">
      <div class="person-name"><strong>Reid</strong> Calloway</div>
      <div class="person-role">Engineer /<br>Director of Operations</div>
    </div>

    <div class="detail-row address">
      <span>248 - 5170 East Hollister<br>Vancouver, BC V5R 2J4</span>
      <svg class="icon" viewBox="0 0 16 16" aria-hidden="true">
        <path d="M8 1a4.5 4.5 0 0 0-4.5 4.5C3.5 9 8 14 8 14s4.5-5 4.5-8.5A4.5 4.5 0 0 0 8 1z" fill="var(--text-white)"/>
        <circle cx="8" cy="5.5" r="1.7" fill="var(--card-black)"/>
      </svg>
    </div>
    <div class="detail-row">
      <span>604.518.2093</span>
      <svg class="icon" viewBox="0 0 16 16" aria-hidden="true">
        <circle cx="8" cy="8" r="7.5" fill="var(--text-white)"/>
        <path d="M5.2 4.2l1.4-.3.8 2-1 .8a5 5 0 0 0 2.9 2.9l.8-1 2 .8-.3 1.4c-3.6.4-7-3-6.6-6.6z" fill="var(--card-black)"/>
      </svg>
    </div>
    <div class="detail-row">
      <span>www.MixVault.com</span>
      <svg class="icon" viewBox="0 0 16 16" aria-hidden="true">
        <circle cx="8" cy="8" r="7" fill="none" stroke="var(--text-white)" stroke-width="1.3"/>
        <ellipse cx="8" cy="8" rx="3" ry="7" fill="none" stroke="var(--text-white)" stroke-width="1"/>
        <line x1="1" y1="8" x2="15" y2="8" stroke="var(--text-white)" stroke-width="1"/>
      </svg>
    </div>
  </div>

  <div class="social-row">
    <span class="social-handle"><span class="social-dot"></span>@MixVault</span>
    <span class="social-handle"><span class="social-dot"></span>@TheMixVault</span>
  </div>
</section>

<section class="card card--back" aria-label="Business card back">
  <div class="brand-mark back-brand">MixVault</div>
</section>

</body>
</html>
```